Non fiction book cover. The book advises how to get a new job.

The book size will be 20cm high by 13cm wide and I need a front cover which can wrap around to the back. This book has a serious message, but I've tried to make it quite light to read and accessible. So I don't want a cover that is too dour or serious and not frivolous either. At the end of the project, I will need a high resolution 3D image of the book, included as part of the package.<br/>The Title of the book is:- "Past Fifty? Hunting for your new role?<br/>by Colin Marsh-Whitby".<br/>I am thinking of a light yellow background, with a striking image to attract attention. The image and words should be clear and sharp.<br/>Here is the, BACK COVER wording.<br/>"This book tells you clearly and simply the steps that you need to take, to get a job, once you’re over 50.<br/>It advises you on the techniques to use to write a killer CV.<br/>It explains how to ensure that your CV attention.<br/>It shows the best way to approach your local job agency.<br/>It demonstrates the best way to use your network.<br/><br/>This book, written by someone with 30 years’ experience in the recruitment industry, gives you ALL the answers.<br/>Whether you are a top executive or someone after some local part time work, then this book is for you. <br/>With the help of this book you will secure your next position.<br/>

Target Market(s)

UK, over 50s, male and female.

Font styles to use
Serif

Colors
fbee3e

Requirements
Must have
• A clear uncluttered cover.
Should not have
• Fussy and over complicated

```html
<!DOCTYPE html>
<html lang="en">
<head>
<meta charset="utf-8">
<title>Past Fifty? Hunting for your new role? — Cover Wrap</title>
<link rel="stylesheet" href="https://fonts.googleapis.com/css2?family=EB+Garamond:wght@400;500;600;700&display=swap">
<style>
  :root {
    --cover-yellow: #fbee3e;
    --title-red: #d4121a;
    --ink: #1a1a1a;
    --stage: #e9e7e3;
    --clock-blue: #2f8fd0;
    --clock-face: #f2f2f2;
    --spine-line: #e3d535;
  }
  * { margin: 0; padding: 0; box-sizing: border-box; }
  html, body {
    width: 1200px;
    height: 1000px;
    overflow: hidden;
    background: var(--stage);
    font-family: "EB Garamond", Garamond, serif;
    color: var(--ink);
  }
  .cover-wrap {
    position: absolute;
    left: 40px;
    top: 92px;
    width: 1120px;
    height: 815px;
    display: flex;
    background: var(--cover-yellow);
    box-shadow: 0 6px 24px rgba(0,0,0,0.18);
  }
  .panel { position: relative; height: 100%; }
  .back-cover { width: 530px; padding: 0 48px; text-align: center; }
  .spine {
    width: 60px;
    border-left: 1px solid var(--spine-line);
    border-right: 1px solid var(--spine-line);
    display: flex;
    justify-content: center;
    padding: 38px 0;
  }
  .front-cover { width: 530px; text-align: center; }

  .title { color: var(--title-red); font-weight: 600; line-height: 1; letter-spacing: -0.01em; }
  .subtitle { text-transform: uppercase; font-weight: 400; line-height: 1.05; }

  .back-cover .title { font-size: 58px; margin-top: 36px; }
  .back-cover .subtitle { font-size: 21px; margin-top: 10px; }
  .blurb {
    margin-top: 38px;
    font-size: 16.5px;
    line-height: 24px;
    text-align: justify;
    hyphens: auto;
  }

  .spine-text {
    writing-mode: vertical-rl;
    display: flex;
    justify-content: space-between;
    align-items: center;
    height: 100%;
    font-size: 15px;
    white-space: nowrap;
  }
  .spine-title { text-transform: uppercase; }
  .spine-title .red { color: var(--title-red); font-weight: 700; }
  .spine-author { font-variant: small-caps; font-weight: 600; font-size: 16px; }

  .front-cover .title { font-size: 86px; margin-top: 100px; }
  .front-cover .subtitle { font-size: 29px; margin-top: 16px; }
  .clock-art {
    position: absolute;
    left: 120px;
    top: 330px;
    width: 290px;
    height: 400px;
  }
  .author {
    position: absolute;
    left: 0; right: 0;
    bottom: 42px;
    font-size: 30px;
    font-weight: 600;
    font-variant: small-caps;
    letter-spacing: 0.01em;
  }
</style>
</head>
<body>
  <main class="cover-wrap">
    <section class="panel back-cover">
      <h2 class="title">PAST FIFTY?</h2>
      <p class="subtitle">Hunting for your<br>new role?</p>
      <p class="blurb">This book tells you clearly and simply the steps that you need to take, to get a job, once you’re over 50. It advises you on the techniques to use to write a killer CV. It explains how to ensure that your CV attention. It shows the best way to approach your local job agency. It demonstrates the best way to use your network. This book, written by someone with 30 years’ experience in the recruitment industry, gives you ALL the answers. Whether you are a top executive or someone after some local part time work, then this book is for you. With the help of this book you will secure your next position.</p>
    </section>

    <section class="panel spine">
      <div class="spine-text">
        <span class="spine-title"><span class="red">Past Fifty?</span> Hunting for your new role?</span>
        <span class="spine-author">Colin Marsh-Whitby</span>
      </div>
    </section>

    <section class="panel front-cover">
      <h1 class="title">PAST FIFTY?</h1>
      <p class="subtitle">Hunting for your<br>new role?</p>
      <svg class="clock-art" viewBox="0 0 290 400" role="img" aria-label="Illustration of a ringing blue alarm clock with a white face">
        <defs>
          <radialGradient id="clockTone" cx="50%" cy="55%" r="55%">
            <stop offset="0%" stop-color="var(--clock-face)"/>
            <stop offset="55%" stop-color="#dfe9f2"/>
            <stop offset="100%" stop-color="var(--clock-blue)"/>
          </radialGradient>
        </defs>
        <ellipse cx="145" cy="205" rx="140" ry="185" fill="url(#clockTone)"/>
      </svg>
      <p class="author">Colin Marsh-Whitby</p>
    </section>
  </main>
</body>
</html>
```